Wadi Alsafeer
Wadi Alsafeer - Construction
Creative Brief
Simple
Salem Dabbagh
CEO
Locality 428 - Alley 17 - House 9 Al Dhaheera - Baghdad - Iraq
ceo@wadialsafeer.com
www.wadialsafeer.com
rokba72x rokba72x
i uploaded the final files so you all can work now with it and very soon I'll chose a winner
and i wont you to make these changes in the latter head only: 1- add the address in Arabic language ( محلة 428 - زقاق 17 - دار 9) and 2- change the e-mail into ( info@wadialsafeer.com ) thank you
Hello , great job all i just wont you to add the name and title in English and Arabic language in the businesses cards only, ( name in Arabic : سالم دباغ) and the title(CEO) in Arabic ( المدير المفوض) Regards,

```html
<!DOCTYPE html>
<html lang="en">
<head>
<meta charset="utf-8">
<title>Wadi Alsafeer – Business Card</title>
<link href="https://fonts.googleapis.com/css2?family=Open+Sans:wght@400;600;700&display=swap" rel="stylesheet">
<style>
  :root {
    --page-bg: #e9eaec;
    --card-bg: #f4f5f6;
    --card-edge: #d6d9dc;
    --brand-blue: #1f7fd8;
    --brand-blue-deep: #1766b4;
    --ink-dark: #3a3f45;
    --ink-soft: #5d646b;
    --white: #ffffff;
    --silver-light: #f2f3f4;
    --silver-mid: #b9bec3;
    --silver-dark: #8d9399;
  }
  * { margin: 0; padding: 0; box-sizing: border-box; }
  html, body {
    width: 1200px; height: 770px; overflow: hidden;
    background: var(--page-bg);
    font-family: "Open Sans", Arial, sans-serif;
  }
  .canvas { position: relative; width: 1200px; height: 770px; }

  .business-card {
    position: absolute; left: 100px; top: 91px;
    width: 1000px; height: 588px;
    background: linear-gradient(160deg, #fbfbfc 0%, var(--card-bg) 55%, #e8eaec 100%);
    border: 1px solid var(--card-edge);
    border-radius: 22px;
    box-shadow: 0 18px 40px rgba(40, 50, 60, 0.18);
    overflow: hidden;
  }

  .brand {
    position: absolute; left: 0; right: 0; top: 150px;
    display: flex; align-items: center; justify-content: center; gap: 18px;
  }
  .brand-square { width: 46px; height: 46px; background: var(--brand-blue); }
  .brand-name {
    font-weight: 700; font-size: 40px; letter-spacing: 4px;
    color: var(--ink-dark); text-transform: uppercase;
  }

  .contact-band {
    position: absolute; left: 0; top: 294px;
    width: 100%; height: 153px;
    background: linear-gradient(180deg, var(--brand-blue) 0%, var(--brand-blue-deep) 100%);
  }
  .band-notch {
    position: absolute; left: 186px; top: -14px;
    width: 0; height: 0;
    border-left: 14px solid transparent;
    border-right: 14px solid transparent;
    border-bottom: 14px solid var(--brand-blue);
  }
  .holder {
    position: absolute; left: 62px; top: 44px; color: var(--white);
  }
  .holder-name { font-size: 26px; font-weight: 600; letter-spacing: 1px; text-transform: uppercase; }
  .holder-title { font-size: 18px; font-weight: 400; margin-top: 4px; }

  .band-divider {
    position: absolute; left: 350px; top: 22px;
    width: 2px; height: 110px; background: rgba(255,255,255,0.75);
  }

  .contact-list {
    position: absolute; left: 386px; top: 14px;
    list-style: none; color: var(--white);
  }
  .contact-list li {
    display: flex; align-items: center; gap: 12px;
    height: 31px; font-size: 17px;
  }
  .contact-icon {
    width: 22px; height: 22px; border-radius: 50%;
    background: var(--white);
    display: flex; align-items: center; justify-content: center;
  }

  .silver-strip {
    position: absolute; left: 0; top: 447px;
    width: 100%; height: 32px;
    background: linear-gradient(90deg, var(--silver-dark) 0%, var(--silver-light) 30%, var(--silver-mid) 55%, var(--silver-light) 80%, var(--silver-dark) 100%);
  }

  .website {
    position: absolute; left: 0; right: 0; top: 500px;
    text-align: center; font-size: 19px; font-weight: 600;
    letter-spacing: 2px; color: var(--ink-soft);
  }
</style>
</head>
<body>
<div class="canvas">
  <div class="business-card">
    <div class="brand">
      <span class="brand-square"></span>
      <span class="brand-name">Wadi Alsafeer</span>
    </div>

    <div class="contact-band">
      <span class="band-notch"></span>
      <div class="holder">
        <p class="holder-name">Omar Rahim</p>
        <p class="holder-title">Managing Director</p>
      </div>
      <span class="band-divider"></span>
      <ul class="contact-list">
        <li>
          <span class="contact-icon">
            <svg width="12" height="12" viewBox="0 0 24 24"><path fill="#2b2f33" d="M6.6 10.8a15.1 15.1 0 0 0 6.6 6.6l2.2-2.2c.3-.3.7-.4 1-.2 1.1.4 2.3.6 3.6.6.6 0 1 .4 1 1V20c0 .6-.4 1-1 1A17 17 0 0 1 3 4c0-.6.4-1 1-1h3.5c.6 0 1 .4 1 1 0 1.3.2 2.5.6 3.6.1.3 0 .7-.2 1z"/></svg>
          </span>
          010 555 0142
        </li>
        <li>
          <span class="contact-icon">
            <svg width="12" height="12" viewBox="0 0 24 24"><path fill="#2b2f33" d="M6.6 10.8a15.1 15.1 0 0 0 6.6 6.6l2.2-2.2c.3-.3.7-.4 1-.2 1.1.4 2.3.6 3.6.6.6 0 1 .4 1 1V20c0 .6-.4 1-1 1A17 17 0 0 1 3 4c0-.6.4-1 1-1h3.5c.6 0 1 .4 1 1 0 1.3.2 2.5.6 3.6.1.3 0 .7-.2 1z"/></svg>
          </span>
          010 555 0142
        </li>
        <li>
          <span class="contact-icon">
            <svg width="12" height="12" viewBox="0 0 24 24"><path fill="#2b2f33" d="M3 6h18v12H3z"/><path fill="none" stroke="#ffffff" stroke-width="2" d="M3 6l9 7 9-7"/></svg>
          </span>
          hello@mailbox.example
        </li>
        <li>
          <span class="contact-icon">
            <svg width="12" height="12" viewBox="0 0 24 24"><path fill="#2b2f33" d="M12 2a7 7 0 0 0-7 7c0 5 7 13 7 13s7-8 7-13a7 7 0 0 0-7-7zm0 9.5a2.5 2.5 0 1 1 0-5 2.5 2.5 0 0 1 0 5z"/></svg>
          </span>
          12 Sample Street Rd, Baghdad
        </li>
      </ul>
    </div>

    <div class="silver-strip"></div>
    <p class="website">www.examplesite.com</p>
  </div>
</div>
</body>
</html>
```